Psychiatrist/ Psychotherapist needs a letterhead design

I am a Psychiatrist working in private practice. I work as a psychotherapist and treat patients with depression, anxiety, post traumatic stress and relationship problems. I need a letterhead which is elegant and professional. I would like to see designs using colours such as blues and greys.
I would like the information on the letterhead split between the top and bottom of the page to give it a look of balance.
I want it to look elegant, feminine and upmarket. I don't want it to look too corporate but to show some flair and to be a bit artistic.

Other doctors, specialists and agencies who have referred patients to me.

Work

Script

Requirements
Must have
• My name and my profession psychiatrist need to be highlighted and prominent. It needs to be professional looking and elegant without being old fashioned or too conservative.
Nice to have
• Balance between the top and bottom of the page.
Should not have
• I don't want fonts which are old and too traditional.

```html
<!DOCTYPE html>
<html lang="en">
<head>
<meta charset="utf-8">
<title>Letterhead – Psychiatrist</title>
<link rel="stylesheet" href="https://fonts.googleapis.com/css2?family=Playfair+Display:ital,wght@1,400&display=swap">
<style>
  :root {
    --sky-deep: #27a0e2;
    --sky-mid: #6ec2ef;
    --sky-pale: #c4e6f8;
    --paper: #ffffff;
    --mark-grey: #e6e6e6;
    --ink-light: #ffffff;
  }
  html, body {
    margin: 0;
    padding: 0;
    overflow: hidden;
    background: var(--paper);
  }
  .letterhead {
    position: relative;
    width: 863px;
    height: 1200px;
    background: var(--paper);
    overflow: hidden;
  }
  .band {
    position: absolute;
    left: 0;
    width: 863px;
  }
  .band svg { display: block; }
  .band--top { top: 0; height: 144px; }
  .band--bottom { bottom: 0; height: 146px; }
  .profession {
    position: absolute;
    margin: 0;
    font-family: "Playfair Display", Georgia, serif;
    font-style: italic;
    font-weight: 400;
    font-size: 26px;
    line-height: 1;
    color: var(--ink-light);
    letter-spacing: -0.3px;
    white-space: nowrap;
  }
  .profession--top { right: 24px; top: 74px; }
  .profession--bottom { left: 47px; top: 90px; }
  .brand-mark {
    position: absolute;
    left: 300px;
    top: 480px;
    width: 260px;
    height: 240px;
    border-radius: 50%;
    background: radial-gradient(circle at 50% 50%, var(--mark-grey) 0%, rgba(230,230,230,0.6) 55%, rgba(230,230,230,0) 72%);
  }
</style>
</head>
<body>
<main class="letterhead">
  <header class="band band--top">
    <svg width="863" height="144" viewBox="0 0 863 144" aria-hidden="true">
      <defs>
        <linearGradient id="skyTop" x1="0" y1="0" x2="0" y2="1">
          <stop offset="0" stop-color="var(--sky-deep)"/>
          <stop offset="0.55" stop-color="var(--sky-mid)"/>
          <stop offset="1" stop-color="var(--sky-pale)"/>
        </linearGradient>
      </defs>
      <rect width="863" height="144" fill="url(#skyTop)"/>
      <path d="M40 0 C200 88 470 132 710 144 L560 144 C380 128 190 78 8 0 Z" fill="var(--paper)"/>
      <path d="M112 0 C290 62 470 98 640 124 C460 104 280 62 146 0 Z" fill="var(--paper)"/>
    </svg>
    <p class="profession profession--top">my profession psychiatrist</p>
  </header>

  <div class="brand-mark" role="img" aria-label="Faint practice emblem placed at the centre of the page"></div>

  <footer class="band band--bottom">
    <svg width="863" height="146" viewBox="0 0 863 146" aria-hidden="true">
      <defs>
        <linearGradient id="skyBottom" x1="0" y1="0" x2="0" y2="1">
          <stop offset="0" stop-color="var(--sky-pale)"/>
          <stop offset="0.45" stop-color="var(--sky-mid)"/>
          <stop offset="1" stop-color="var(--sky-deep)"/>
        </linearGradient>
      </defs>
      <rect width="863" height="146" fill="url(#skyBottom)"/>
      <path d="M160 0 C430 10 700 70 863 146 L863 124 C700 52 460 6 260 0 Z" fill="var(--paper)"/>
      <path d="M520 0 C680 30 800 78 863 108 L863 94 C790 58 680 24 566 0 Z" fill="var(--paper)"/>
    </svg>
    <p class="profession profession--bottom">my profession psychiatrist</p>
  </footer>
</main>
</body>
</html>
```